Website for the Careway Kiosk (sm): A mobile station with first aid supplies, staffed by our medics!

Hi! We need to create a new website. Will also need to be able to control the back-end - we need to be able to control and change the site easily, perhaps with css? This will be an offering from our company, Lanternfield Advisory LLC. We want this site to reflect the service: a mobile Careway Kiosk, staffed with our medics (see attached photo) - we will be hired to work at parties, children's birthday parties, sporting events, road races and triathlons, weddings, etc. We want companies, corporations and event planners to hire us! We will need 4 or 5 tabs/links to illustrate our offerings. We like warm colors and brightness - light and inviting, to attract attention. As you see, our company logo is blue - but the front panel illustration is a velum insert and may be changed to any theme. The final design should communicate that you should never plan an event without one of our Careway Kiosks! We want the site to be inviting, like some of these referenced below:

OUR FAVORITE (Especially if the bottles on the home page were actually links) mirela-demo.pagewrightly.com

Others we like:

https://www.pagewrightly.com/templates/food-drink

tundra-demo.pagewrightly.com

https://www.kinhavenmag.com/

https://www.zippazappa.com/

https://www.ottersandteacups.com/

Target Market(s)

Event Planners, Wedding Coordinators, Large corporations, Sports Event Managers, Fun Run/Triathlon Coordinators, Parents, Health and Safety Managers

Coding

Coded - Design and coding required

Number of Pages Required

4 page

Font styles to use
Sans Serif
Other font styles liked:
• Calibri

Colors

Requirements
Must have
• Warm, inviting colors, 4 or 5 tabs/links, our logo, easy to navigate, the ability to be easily altered, room for photos.
• Must be able to link to our other company website: www.lanternfieldadvisoryllc.com
Should not have
• Boring fonts, darkness, difficulty with naviation

```html
<!DOCTYPE html>
<html lang="en">
<head>
<meta charset="utf-8">
<title>Careway Kiosk</title>
<link rel="stylesheet" href="https://fonts.googleapis.com/css2?family=Poppins:wght@300;400;500;600&display=swap">
<style>
:root{
  --navy:#0b0f73;
  --ink:#1b1b1b;
  --body:#5e5e5e;
  --rule:#dcdcdc;
  --white:#ffffff;
  --orange:#f7941d;
  --footer:#1b1b1b;
  --footer-text:#cfcfcf;
}
*{margin:0;padding:0;box-sizing:border-box}
html,body{width:1200px;height:3711px;overflow:hidden}
body{position:relative;background:var(--white);font-family:"Poppins",sans-serif;color:var(--ink)}
.abs{position:absolute}

/* header */
.social{left:87px;top:56px;display:flex;gap:12px}
.social span{width:26px;height:26px;border-radius:50%;display:block}
.social span:nth-child(1){background:#3b5998}
.social span:nth-child(2){background:#3ca7e4}
.social span:nth-child(3){background:#1b73ad}
.social span:nth-child(4){background:#dd4b39}
.social span:nth-child(5){background:#d32323}
.brand{left:0;width:1200px;top:42px;display:flex;justify-content:center;align-items:center;gap:14px}
.brand .dot{width:52px;height:52px;border-radius:50%;background:var(--navy)}
.brand .name{font-size:30px;font-weight:600;color:var(--navy);line-height:1}
.phone{right:87px;top:56px;font-size:20px;font-weight:500;color:var(--navy);display:flex;align-items:center;gap:8px}
.nav-rule{left:87px;width:1026px;top:143px;height:2px;background:var(--rule)}
.nav{left:0;width:1200px;top:156px;display:flex;justify-content:center}
.nav a{font-size:15px;color:var(--ink);text-decoration:none;padding:0 35px}

/* hero */
.hero{left:0;top:213px;width:1200px;height:497px;background:linear-gradient(120deg,#6d2a2a 0%,#8a3a34 30%,#5c5f63 60%,#33455f 100%)}
.hero-shade{left:0;top:213px;width:1200px;height:497px;background:rgba(0,0,0,.28)}
.hero-title{left:0;width:1200px;top:330px;text-align:center;color:var(--white);font-size:96px;font-weight:400;line-height:1.1}
.hero-sub{left:0;width:1200px;top:518px;text-align:center;color:var(--white);font-size:22px;font-weight:400}
.dots{left:0;width:1200px;top:625px;display:flex;justify-content:center;gap:6px}
.dots span{width:14px;height:14px;border-radius:50%;border:2px solid var(--white)}
.dots span.on{background:var(--navy)}

/* welcome */
.welcome-title{left:0;width:1200px;top:790px;text-align:center;font-size:33px;font-weight:500;letter-spacing:6px;line-height:1.3}
.welcome-copy{left:190px;width:820px;top:862px;text-align:center;font-size:12.5px;line-height:28px;color:var(--body)}
.btn-solid{left:512px;top:1014px;width:173px;height:62px;background:var(--navy);color:var(--white);font-size:16px;display:flex;align-items:center;justify-content:center;gap:8px}

/* services */
.card-img{width:490px;height:279px;border-radius:4px}
.card-title{font-size:16px;font-weight:600}
.card-copy{width:480px;font-size:12px;line-height:26px;color:var(--body)}
.btn-outline{width:123px;height:49px;border:2px solid var(--navy);border-radius:3px;color:var(--navy);font-size:11px;display:flex;align-items:center;justify-content:center}

/* testimonial */
.testi{left:0;top:2271px;width:1200px;height:322px;background:linear-gradient(90deg,#3d3935,#4b4540 50%,#3a3632)}
.testi-shade{left:0;top:2271px;width:1200px;height:322px;background:rgba(0,0,0,.35)}
.testi-title{left:0;width:1200px;top:2318px;text-align:center;color:var(--white);font-size:30px;font-weight:500;line-height:1.3}
.avatar{left:89px;top:2402px;width:128px;height:128px;border-radius:50%;border:4px solid var(--white);background:linear-gradient(160deg,#b9b0a8,#6a5e58)}
.testi-body{left:286px;width:810px;top:2398px;color:var(--white)}
.testi-copy{font-size:14px;line-height:28px}
.testi-name{margin-top:12px;font-size:17px;line-height:24px}

/* gallery */
.tile{border-radius:2px}
.tile-label{color:var(--white);font-weight:500;line-height:1.2}

/* footer */
.footer{left:0;top:3347px;width:1200px;height:364px;background:var(--footer)}
.f-brand{left:87px;top:3418px;display:flex;align-items:center;gap:12px}
.f-brand .dot{width:44px;height:44px;border-radius:50%;background:var(--navy);border:2px solid var(--white)}
.f-brand .name{font-size:24px;font-weight:600;color:var(--white)}
.f-partner{left:87px;top:3540px;width:280px;text-align:center;color:var(--white);font-size:21px;font-weight:400}
.f-partner-sub{left:87px;top:3600px;width:280px;text-align:center;color:var(--footer-text);font-size:10px}
.f-head{top:3408px;color:var(--white);font-size:16px;font-weight:500;letter-spacing:.5px}
.f-links{left:438px;top:3448px;list-style:none}
.f-links li{color:var(--footer-text);font-size:13px;line-height:29px}
.f-note{left:621px;top:3448px;width:260px;color:var(--footer-text);font-size:13px;line-height:21px}
.f-input{left:621px;top:3506px;width:258px;height:36px;background:var(--white);color:#666;font-size:12px;padding:0 12px;display:flex;align-items:center}
.f-btn{left:621px;top:3562px;width:100px;height:32px;background:var(--orange);color:var(--white);font-size:12px;display:flex;align-items:center;justify-content:center;border-radius:2px}
.f-contact{left:943px;top:3448px}
.f-contact .row{display:flex;gap:18px;color:var(--footer-text);font-size:13px;line-height:21px;margin-bottom:18px}
.f-rule{left:87px;width:1026px;top:3637px;height:1px;background:#3a3a3a}
.copyright{left:87px;top:3660px;color:var(--footer-text);font-size:12px}
.f-social{right:87px;top:3656px;display:flex;gap:8px}
.f-social span{width:26px;height:26px;border-radius:50%;border:1px solid var(--footer-text)}
</style>
</head>
<body>

<header>
  <div class="abs social" aria-label="Social links"><span></span><span></span><span></span><span></span><span></span></div>
  <div class="abs brand"><span class="dot"></span><span class="name">Careway Kiosk</span></div>
  <div class="abs phone">
    <svg width="18" height="18" viewBox="0 0 24 24"><path fill="#0b0f73" d="M6.6 10.8a15 15 0 0 0 6.6 6.6l2.2-2.2c.3-.3.7-.4 1-.2 1.1.4 2.3.6 3.6.6.6 0 1 .4 1 1V20c0 .6-.4 1-1 1A17 17 0 0 1 3 4c0-.6.4-1 1-1h3.5c.6 0 1 .4 1 1 0 1.3.2 2.5.6 3.6.1.3 0 .7-.2 1z"/></svg>
    (123) 456-7890
  </div>
  <div class="abs nav-rule"></div>
  <nav class="abs nav"><a>Home</a><a>About Us</a><a>Services</a><a>News</a><a>Contact Us</a></nav>
</header>

<section>
  <div class="abs hero" role="img" aria-label="Photo of a medic giving first aid to an injured cyclist on a road"></div>
  <div class="abs hero-shade"></div>
  <div class="abs hero-title">Careway Kiosk</div>
  <div class="abs hero-sub">Powered by Lanternfield Advisory LLC</div>
  <div class="abs dots"><span></span><span></span><span class="on"></span><span></span></div>
</section>

<section>
  <h1 class="abs welcome-title">WELCOME TO THE CAREWAY KIOSK</h1>
  <p class="abs welcome-copy">Lorem Ipsum is simply dummy text of the printing and typesetting industry. Lorem Ipsum has been the industry's standard dummy text ever since the 1500s, when an unknown printer took a galley of type and scrambled it to make a type specimen book. It has survived not only five centuries, but also the leap into electronic typesetting, remaining essentially unchanged. It was popularised in the 1960s with the release of Letraset sheets containing Lorem Ipsum passages, and more recently with desktop publishing software like Aldus PageMaker including versions of Lorem Ipsum.</p>
  <div class="abs btn-solid">Read More <span>›</span></div>
</section>

<section>
  <div class="abs card-img" style="left:87px;top:1168px;background:linear-gradient(135deg,#3a1b4f,#8d3a6d 50%,#2a2f6a)" role="img" aria-label="Photo of guests celebrating at a party with confetti"></div>
  <div class="abs card-title" style="left:87px;top:1472px">CELEBRATIONS</div>
  <p class="abs card-copy" style="left:87px;top:1500px">Accusantium doloremque laudantium, totam rem aperiam, eaque ipsa quae ab illo inventore veritatis et quasi architecto beatae vitae dicta sunt cabo. Nemo enim ipsam voluptatem quia voluptas...</p>
  <div class="abs btn-outline" style="left:87px;top:1596px">LEARN MORE</div>

  <div class="abs card-img" style="left:621px;top:1168px;background:linear-gradient(180deg,#b5c7d6,#6f7a82 60%,#4a4e52)" role="img" aria-label="Photo of cyclists racing on a road"></div>
  <div class="abs card-title" style="left:621px;top:1472px">SPORTING EVENTS</div>
  <p class="abs card-copy" style="left:621px;top:1500px">Accusantium doloremque laudantium, totam rem aperiam, eaque ipsa quae ab illo inventore veritatis et quasi architecto beatae vitae dicta sunt cabo. Nemo enim ipsam voluptatem quia voluptas...</p>
  <div class="abs btn-outline" style="left:621px;top:1596px">LEARN MORE</div>

  <div class="abs card-img" style="left:87px;top:1712px;background:linear-gradient(180deg,#8a8a86,#4e4d4b 55%,#d8d5d0)" role="img" aria-label="Photo of a bride and groom walking with wedding guests"></div>
  <div class="abs card-title" style="left:87px;top:2016px">WEDDINGS</div>
  <p class="abs card-copy" style="left:87px;top:2044px">Accusantium doloremque laudantium, totam rem aperiam, eaque ipsa quae ab illo inventore veritatis et quasi architecto beatae vitae dicta sunt cabo. Nemo enim ipsam voluptatem quia voluptas...</p>
  <div class="abs btn-outline" style="left:87px;top:2142px">LEARN MORE</div>

  <div class="abs card-img" style="left:621px;top:1712px;background:linear-gradient(180deg,#f3d9a0,#e98f5a 50%,#f2b64a)" role="img" aria-label="Photo of children cheering at a birthday party with balloons"></div>
  <div class="abs card-title" style="left:621px;top:2016px">CHILDREN'S PARTIES</div>
  <p class="abs card-copy" style="left:621px;top:2044px">Accusantium doloremque laudantium, totam rem aperiam, eaque ipsa quae ab illo inventore veritatis et quasi architecto beatae vitae dicta sunt cabo. Nemo enim ipsam voluptatem quia voluptas...</p>
  <div class="abs btn-outline" style="left:621px;top:2142px">LEARN MORE</div>
</section>

<section>
  <div class="abs testi" role="img" aria-label="Background photo of a cafe interior"></div>
  <div class="abs testi-shade"></div>
  <h2 class="abs testi-title">TESTIMONIALS &amp; ENDORSEMENTS</h2>
  <svg class="abs" style="left:18px;top:2416px" width="20" height="34" viewBox="0 0 20 34"><path d="M17 2 3 17l14 15" fill="none" stroke="#fff" stroke-width="3"/></svg>
  <svg class="abs" style="left:1162px;top:2416px" width="20" height="34" viewBox="0 0 20 34"><path d="M3 2l14 15L3 32" fill="none" stroke="#fff" stroke-width="3"/></svg>
  <div class="abs avatar" role="img" aria-label="Portrait photo of the client giving the testimonial"></div>
  <div class="abs testi-body">
    <p class="testi-copy">Lorem Ipsum is simply dummy text of the printing and typesetting industry. Lorem Ipsum has been the industry's standard dummy text ever since the 1500s, when an unknown printer took a galley of type and scrambled it to make a type specimen book. It has survived not only five centuries, but also the leap into elunchanged.</p>
    <div class="testi-name">– Marisol T. Quenby.</div>
  </div>
</section>

<section>
  <div class="abs tile" style="left:87px;top:2640px;width:601px;height:643px;background:linear-gradient(160deg,#3b3632,#5a2a2a 50%,#2b2b2d)" role="img" aria-label="Photo of a road race cyclist close up"></div>
  <div class="abs tile-label" style="left:118px;top:2664px;font-size:28px">ROAD RACES</div>
  <div class="abs tile" style="left:730px;top:2640px;width:383px;height:299px;background:linear-gradient(180deg,#1f6f96,#3a9bc2 55%,#17587d)" role="img" aria-label="Photo of triathlon swimmers in open water"></div>
  <div class="abs tile-label" style="left:770px;top:2882px;font-size:15px">TRIATHLONS</div>
  <div class="abs tile" style="left:730px;top:2984px;width:383px;height:299px;background:linear-gradient(180deg,#6b5e6a,#8b7b86 55%,#5a5058)" role="img" aria-label="Photo of a wedding couple in front of a floral wall"></div>
  <div class="abs tile-label" style="left:776px;top:3226px;font-size:15px">WEDDINGS</div>
</section>

<footer>
  <div class="abs footer"></div>
  <div class="abs f-brand"><span class="dot"></span><span class="name">Careway Kiosk</span></div>
  <div class="abs f-partner">Lanternfield Advisory</div>
  <div class="abs f-partner-sub">Careway Kiosk, Powered by Lanternfield Advisory LLC</div>

  <div class="abs f-head" style="left:438px">QUICK LINKS</div>
  <ul class="abs f-links"><li>Home</li><li>About Us</li><li>Careway Kiosk Services</li><li>News</li><li>Contact Us</li></ul>

  <div class="abs f-head" style="left:621px">NEWSLETTER SUBSCRIPTION</div>
  <p class="abs f-note">Register your Email Address to get information about us</p>
  <div class="abs f-input">Email Address</div>
  <div class="abs f-btn">SUBSCRIBE</div>

  <div class="abs f-head" style="left:943px">CONTACT US</div>
  <div class="abs f-contact">
    <div class="row"><svg width="14" height="18" viewBox="0 0 14 18"><path d="M7 0a7 7 0 0 0-7 7c0 5 7 11 7 11s7-6 7-11a7 7 0 0 0-7-7zm0 9.5A2.5 2.5 0 1 1 7 4.5a2.5 2.5 0 0 1 0 5z" fill="#fff"/></svg><span>PO Box 4417, Harlow Vale<br>NSW 2090 Australia</span></div>
    <div class="row"><svg width="14" height="14" viewBox="0 0 24 24"><path fill="#fff" d="M6.6 10.8a15 15 0 0 0 6.6 6.6l2.2-2.2c.3-.3.7-.4 1-.2 1.1.4 2.3.6 3.6.6.6 0 1 .4 1 1V20c0 .6-.4 1-1 1A17 17 0 0 1 3 4c0-.6.4-1 1-1h3.5c.6 0 1 .4 1 1 0 1.3.2 2.5.6 3.6.1.3 0 .7-.2 1z"/></svg><span>+1 888 888 8888</span></div>
    <div class="row"><svg width="15" height="12" viewBox="0 0 15 12"><rect width="15" height="12" rx="1" fill="#fff"/><path d="M1 1l6.5 5L14 1" fill="none" stroke="#1b1b1b" stroke-width="1.3"/></svg><span>info@carewaykiosk.com</span></div>
  </div>

  <div class="abs f-rule"></div>
  <div class="abs copyright">Copyrights © 2017, Careway Kiosk . All rights reserved.</div>
  <div class="abs f-social"><span></span><span></span><span></span><span></span></div>
</footer>

</body>
</html>
```